Still River Way - Business Card

May try various combos of colors from primary & secondary palette attached below. Logo and Catch phrase previous built logo attached should go on front, but change to color palette options noted. may try various color options from minimal to zen like quality/vibe.
On Front: Attached Logo & Phrase
On Back:
https://stillriverway.com/
415.555.0193
stillriverway@theremotehelpers.ai

Contact Information for Business Card

Gregory T. Lund, MD Founder & CEO https://stillriverway.com/ 415.555.0193 stillriverway@theremotehelpers.ai

```html
<!DOCTYPE html>
<html lang="en">
<head>
<meta charset="utf-8">
<title>Still River Way – Business Card</title>
<link rel="stylesheet" href="https://fonts.googleapis.com/css2?family=Montserrat:wght@300;400;500;700&family=Tinos:wght@400&display=swap">
<style>
  :root {
    --backdrop: #d3d3d3;
    --forest: #2f5718;
    --forest-deep: #284b14;
    --paper: #f3f3f0;
    --ink-grey: #6d6d6d;
    --white: #ffffff;
  }
  html, body {
    margin: 0;
    padding: 0;
    width: 1200px;
    height: 1051px;
    overflow: hidden;
    background: var(--backdrop);
  }
  .sheet {
    width: 1200px;
    height: 1051px;
    display: flex;
    flex-direction: column;
    align-items: center;
    justify-content: center;
    gap: 60px;
  }
  .card {
    width: 760px;
    height: 434px;
    box-sizing: border-box;
    box-shadow: 0 6px 18px rgba(0,0,0,0.12);
    display: flex;
    flex-direction: column;
    align-items: center;
    justify-content: center;
  }
  /* Front */
  .card--front {
    background: var(--forest);
    color: var(--white);
  }
  .brand {
    display: flex;
    align-items: center;
    gap: 22px;
  }
  .brand__mark {
    width: 70px;
    height: 70px;
    border: 2px solid var(--white);
    border-radius: 50%;
    box-sizing: border-box;
  }
  .brand__name {
    font-family: "Tinos", "Times New Roman", serif;
    font-size: 58px;
    font-weight: 400;
    line-height: 1;
    color: var(--white);
  }
  .brand__tagline {
    margin: 18px 0 0;
    font-family: "Montserrat", sans-serif;
    font-weight: 400;
    font-size: 21px;
    letter-spacing: 0.3px;
    color: var(--white);
  }
  /* Back */
  .card--back {
    background: var(--paper);
    border-bottom: 3px solid var(--forest-deep);
    font-family: "Montserrat", sans-serif;
    text-align: center;
  }
  .contact__name {
    margin: 0;
    font-weight: 700;
    font-size: 25px;
    letter-spacing: 0.8px;
    color: var(--forest);
    text-transform: uppercase;
  }
  .contact__title {
    margin: 6px 0 0;
    font-weight: 400;
    font-size: 17px;
    color: var(--ink-grey);
  }
  .contact__rule {
    width: 70px;
    height: 0;
    border: none;
    border-top: 1.5px solid var(--forest);
    margin: 30px auto 28px;
  }
  .contact__line {
    margin: 0;
    font-weight: 300;
    font-size: 17px;
    line-height: 1.55;
    color: var(--ink-grey);
    letter-spacing: 0.3px;
  }
  .contact__line strong {
    font-weight: 500;
    color: var(--forest);
  }
</style>
</head>
<body>
  <main class="sheet">
    <section class="card card--front" aria-label="Card front">
      <div class="brand">
        <span class="brand__mark" aria-hidden="true"></span>
        <span class="brand__name">Still River Way</span>
      </div>
      <p class="brand__tagline">Nurturing Calm Hearts, Minds &amp; Souls</p>
    </section>

    <section class="card card--back" aria-label="Card back">
      <h1 class="contact__name">Gregory T. Lund, MD</h1>
      <p class="contact__title">Founder &amp; CEO</p>
      <hr class="contact__rule">
      <p class="contact__line">415.555.0193</p>
      <p class="contact__line">stillriverway@theremotehelpers.ai</p>
      <p class="contact__line">www.<strong>stillriverway</strong>.com</p>
    </section>
  </main>
</body>
</html>
```